Young and modern Electrical company working in the commercial arena.

Wanting a business card design thats modern and will last. Maybe Minimalist? Happy to look at changing my logo

Target Market(s)

Builders, Project Managers

Industry/Entity Type

Electrical

Contact Information for Business Card

Name
Address
Phone number
Job title

Logo Text

our name or just the logo i'm open to ideas

Font styles to use
Sans Serif

Requirements
Nice to have
• would like to keep the purple in our current logo. it's kinda unique to our market
Should not have
• Don't want it to be to busy. simple is best i think

```html
<!DOCTYPE html>
<html lang="en">
<head>
<meta charset="utf-8">
<title>Halvern Electrical — Business Card</title>
<link href="https://fonts.googleapis.com/css2?family=Montserrat:wght@500;600&family=Lato:wght@400&display=swap" rel="stylesheet">
<style>
  :root {
    --purple: #6a0fc9;
    --purple-soft: #7a24d4;
    --ink: #2f2f33;
    --grey-band: #3a3a3d;
    --paper: #ffffff;
    --backdrop: #e6e6e8;
  }
  * { margin: 0; padding: 0; box-sizing: border-box; }
  html, body { width: 1200px; height: 782px; overflow: hidden; }
  body {
    background: var(--backdrop);
    position: relative;
    font-family: "Lato", sans-serif;
    color: var(--ink);
  }
  .card {
    position: absolute;
    width: 540px;
    height: 309px;
    top: 236px;
    overflow: hidden;
    box-shadow: 0 6px 18px rgba(0,0,0,0.18);
  }
  .card-front { left: 40px; background: var(--paper); }
  .card-back { left: 620px; background: var(--purple); }

  .holder { position: absolute; left: 34px; top: 30px; }
  .holder-name {
    font-family: "Montserrat", sans-serif;
    font-weight: 500;
    font-size: 18px;
    letter-spacing: 1.5px;
    text-transform: uppercase;
    color: var(--ink);
  }
  .holder-name .first { color: var(--purple); }
  .holder-role { font-size: 11px; margin-top: 2px; color: var(--ink); }

  .brand {
    position: absolute;
    left: 250px;
    top: 118px;
    display: flex;
    align-items: center;
    gap: 12px;
  }
  .brand-square { width: 16px; height: 16px; background: var(--purple); flex: none; }
  .brand-name {
    font-family: "Montserrat", sans-serif;
    font-weight: 600;
    font-size: 24px;
    line-height: 1.05;
    letter-spacing: 1px;
    text-transform: uppercase;
    color: var(--purple);
  }

  .contact { position: absolute; left: 34px; top: 172px; list-style: none; font-size: 13px; }
  .contact li { display: flex; align-items: center; gap: 7px; margin-bottom: 4px; }
  .contact svg { width: 11px; height: 11px; fill: var(--purple); flex: none; }

  .address {
    position: absolute;
    right: 34px;
    bottom: 36px;
    font-size: 14px;
    line-height: 1.35;
    text-align: right;
  }
  .band { position: absolute; left: 0; bottom: 0; width: 540px; height: 24px; }

  .back-pattern { position: absolute; inset: 0; background: var(--purple-soft); }
  .back-brand {
    position: absolute;
    inset: 0;
    display: flex;
    align-items: center;
    justify-content: center;
    font-family: "Montserrat", sans-serif;
    font-weight: 600;
    font-size: 20px;
    letter-spacing: 1.5px;
    text-transform: uppercase;
    color: var(--paper);
  }
</style>
</head>
<body>
  <section class="card card-front">
    <div class="holder">
      <p class="holder-name"><span class="first">Marcus</span> Bell</p>
      <p class="holder-role">Managing Director</p>
    </div>

    <div class="brand">
      <span class="brand-square"></span>
      <p class="brand-name">Halvern<br>Electrical</p>
    </div>

    <ul class="contact">
      <li>
        <svg viewBox="0 0 24 24" aria-hidden="true"><path d="M6.6 10.8a15.1 15.1 0 0 0 6.6 6.6l2.2-2.2a1 1 0 0 1 1-.25 11.4 11.4 0 0 0 3.6.57 1 1 0 0 1 1 1V20a1 1 0 0 1-1 1A17 17 0 0 1 3 4a1 1 0 0 1 1-1h3.5a1 1 0 0 1 1 1c0 1.25.2 2.45.57 3.57a1 1 0 0 1-.25 1z"/></svg>
        044-555 018 273
      </li>
      <li>
        <svg viewBox="0 0 24 24" aria-hidden="true"><path d="M2 5h20v14H2z M2 5l10 8 10-8" fill="var(--purple)"/><path d="M2 5l10 8 10-8" stroke="#fff" stroke-width="2" fill="none"/></svg>
        info@halvernelec.com
      </li>
    </ul>

    <p class="address">88, Linden Road<br>Northfield, 20418</p>

    <svg class="band" viewBox="0 0 540 24" aria-hidden="true">
      <polygon points="0,0 282,0 298,24 0,24" fill="var(--purple)"/>
      <polygon points="290,12 540,12 540,24 298,24" fill="var(--grey-band)"/>
    </svg>
  </section>

  <section class="card card-back">
    <div class="back-pattern" role="img" aria-label="Repeating faint brand monogram pattern across the purple card back"></div>
    <p class="back-brand">Halvern Electrical</p>
  </section>
</body>
</html>
```